Debt Relief Landing Page Design

I need a landing page designed (and the accompanying Thank You page) for my client.

I have drafted the wireframes for the layout of the pages (attached) and need a professional looking finish.

The main colours to use are green and blue as per their current branding, see website for specifications - http://www.clearpathledger.com.au/

```html
<!DOCTYPE html>
<html lang="en">
<head>
<meta charset="utf-8">
<title>Clear Path Ledger – Debt Consolidation</title>
<link href="https://fonts.googleapis.com/css2?family=Open+Sans:ital,wght@0,400;0,600;0,700;0,800;1,400&family=Montserrat:wght@500;600;700&display=swap" rel="stylesheet">
<style>
:root{
  --navy:#1c355e;
  --navy-deep:#142847;
  --blue:#1f4f8f;
  --icon-blue:#1d5aa6;
  --green:#6aa83a;
  --green-dark:#5a9430;
  --text:#4a4a4a;
  --muted:#7a7a7a;
  --light:#f4f5f7;
  --white:#ffffff;
  --footer:#1a2d4d;
}
*{box-sizing:border-box;margin:0;padding:0}
html,body{width:763px;height:1200px;overflow:hidden}
body{font-family:"Open Sans",Arial,sans-serif;color:var(--text);background:var(--white)}
.page{width:763px;height:1200px;position:relative}

/* header */
.site-header{height:64px;display:flex;align-items:center;justify-content:space-between;padding:0 40px;background:var(--white)}
.brand{display:flex;align-items:center;gap:8px;font-family:"Open Sans",Arial,sans-serif;font-weight:800;font-size:25px;color:var(--navy)}
.brand-mark{width:14px;height:14px;border-radius:50%;background:var(--green)}
.header-contact{display:flex;align-items:center;gap:8px;font-size:11px;font-weight:600;color:var(--navy);letter-spacing:.5px}
.header-contact .phone{color:var(--blue);font-size:12px;font-weight:700}

/* hero */
.hero{height:296px;position:relative;text-align:center;color:var(--white);padding-top:30px;
  background:linear-gradient(180deg,#2a4a78 0%,#1f3d68 55%,#1a3459 100%)}
.hero-title{font-family:"Montserrat",Arial,sans-serif;font-weight:500;font-size:25px;letter-spacing:.5px}
.hero-sub{font-family:"Montserrat",Arial,sans-serif;font-size:15px;font-weight:500;line-height:1.35;margin-top:12px}
.hero-copy{width:560px;margin:14px auto 0;font-size:8.5px;line-height:1.5;color:#dfe6f1}
.hero-copy p+p{margin-top:8px}
.btn{display:inline-block;background:var(--green);color:var(--white);font-family:"Montserrat",Arial,sans-serif;font-weight:600;font-size:14px;letter-spacing:.3px;border-radius:20px;padding:10px 26px}
.hero .btn{margin-top:20px}

/* services */
.services{height:375px;padding-top:30px;text-align:center;background:var(--white)}
.section-title{font-family:"Montserrat",Arial,sans-serif;font-weight:600;font-size:17px;color:var(--navy);letter-spacing:.3px}
.section-title .accent{color:var(--green)}
.title-rule{width:440px;height:1px;background:#d8dce2;margin:12px auto 0}
.service-grid{width:640px;margin:24px auto 0;display:grid;grid-template-columns:repeat(3,1fr);row-gap:26px;column-gap:26px}
.service{display:flex;flex-direction:column;align-items:center}
.service-icon{width:44px;height:44px;border-radius:50%;background:var(--icon-blue);display:flex;align-items:center;justify-content:center}
.service-name{margin-top:10px;font-size:10px;font-weight:700;color:var(--blue);text-transform:uppercase;letter-spacing:.3px}
.service-text{margin-top:6px;font-size:8.5px;line-height:1.5;color:var(--muted);width:170px}

/* testimonials */
.testimonials{height:190px;background:var(--light);padding-top:20px;text-align:center;position:relative}
.testimonials .section-title{font-size:16px;font-weight:500}
.quote-row{width:660px;margin:18px auto 0;display:flex;gap:26px;text-align:left}
.quote-card{flex:1}
.quote-head{display:flex;align-items:center;gap:12px}
.avatar{width:46px;height:46px;border-radius:50%;background:radial-gradient(circle at 50% 40%,#c9a98e,#6c7d8e);border:3px solid var(--white)}
.quote-name{font-size:9.5px;font-weight:700;color:var(--navy)}
.quote-text{margin-top:10px;font-size:8.5px;line-height:1.55;color:var(--muted);font-style:italic}
.arrow{position:absolute;top:105px;width:18px;height:18px;border-radius:50%;border:1px solid #b8bec7;display:flex;align-items:center;justify-content:center;background:var(--white)}
.arrow.prev{left:18px}.arrow.next{right:18px}

/* consultation form */
.consultation{height:247px;padding-top:20px;text-align:center;
  background:linear-gradient(180deg,#aab3bd 0%,#8d98a6 60%,#7d8896 100%)}
.consultation .form-title{font-family:"Montserrat",Arial,sans-serif;font-size:19px;font-weight:500;color:var(--white)}
.consultation .form-title .accent{color:#cfe8b6}
.form-intro{font-size:8.5px;color:var(--white);margin-top:12px}
.lead-form{width:340px;margin:12px auto 0;display:grid;grid-template-columns:1fr 1fr;gap:7px 12px}
.field{height:20px;background:var(--white);border:1px solid #d2d6db;font-size:8px;color:#9aa0a8;text-align:left;padding:5px 7px}
.consultation .btn{margin-top:16px}

/* footer */
.site-footer{height:28px;background:var(--footer);color:#c6cfdc;font-size:8.5px;display:flex;align-items:center;justify-content:center}
</style>
</head>
<body>
<div class="page">

  <header class="site-header">
    <div class="brand"><span class="brand-mark"></span>Clear Path Ledger</div>
    <div class="header-contact">
      <span>CONTACT US ON</span>
      <svg width="12" height="12" viewBox="0 0 24 24" aria-hidden="true"><path fill="#1f4f8f" d="M6.6 10.8a15.1 15.1 0 0 0 6.6 6.6l2.2-2.2a1 1 0 0 1 1-.25 11.4 11.4 0 0 0 3.6.57 1 1 0 0 1 1 1V20a1 1 0 0 1-1 1A17 17 0 0 1 3 4a1 1 0 0 1 1-1h3.5a1 1 0 0 1 1 1c0 1.25.2 2.45.57 3.57a1 1 0 0 1-.25 1z"/></svg>
      <span class="phone">1300-555-014</span>
    </div>
  </header>

  <section class="hero" role="img" aria-label="Photo of a person reviewing finances, under a deep blue overlay">
    <h1 class="hero-title">LOOKING TO CONSOLIDATE YOUR DEBTS?</h1>
    <p class="hero-sub">If You Have Over $10,000 In Debt, We Can Help<br>You Be Debt Free In 3-5 years.</p>
    <div class="hero-copy">
      <p>We help Australians take back control of their finances with practical, tailored plans. Our team works with your creditors to reduce pressure and build a single affordable repayment you can manage.</p>
      <p>Speak with one of our friendly specialists today to find out which option suits your situation best. There is no cost and no obligation.</p>
    </div>
    <span class="btn">GET MY FREE CONSULTATION</span>
  </section>

  <section class="services">
    <h2 class="section-title">HERE ARE JUST SOME OF <span class="accent">OUR DEBT RELIEF SERVICES</span></h2>
    <div class="title-rule"></div>
    <div class="service-grid">
      <div class="service">
        <div class="service-icon"><svg width="22" height="22" viewBox="0 0 24 24" aria-hidden="true"><circle cx="12" cy="12" r="8" fill="none" stroke="#fff" stroke-width="2"/><path d="M12 7v10M9.5 9.5h4a1.5 1.5 0 0 1 0 3h-3a1.5 1.5 0 0 0 0 3h4" fill="none" stroke="#fff" stroke-width="1.6"/></svg></div>
        <div class="service-name">Debt Consolidation Loan</div>
        <p class="service-text">Stop getting hassled by creditors. Let us consolidate your debts into one easy repayment plan.</p>
      </div>
      <div class="service">
        <div class="service-icon"><svg width="22" height="22" viewBox="0 0 24 24" aria-hidden="true"><path d="M3 12 12 4l9 8M6 10v9h12v-9" fill="none" stroke="#fff" stroke-width="2" stroke-linejoin="round"/><rect x="10" y="13" width="4" height="6" fill="#fff"/></svg></div>
        <div class="service-name">Mortgage Refinance</div>
        <p class="service-text">Consolidate your debt into an available home loan equity, significantly reducing your monthly repayments.</p>
      </div>
      <div class="service">
        <div class="service-icon"><svg width="22" height="22" viewBox="0 0 24 24" aria-hidden="true"><path d="M6 3h9l4 4v14H6z" fill="none" stroke="#fff" stroke-width="2" stroke-linejoin="round"/><path d="M9 11h7M9 14h7M9 17h5" stroke="#fff" stroke-width="1.6"/></svg></div>
        <div class="service-name">Debt Agreements</div>
        <p class="service-text">A viable alternative to bankruptcy and debt consolidation loans for those struggling to pay.</p>
      </div>
      <div class="service">
        <div class="service-icon"><svg width="22" height="22" viewBox="0 0 24 24" aria-hidden="true"><path d="M12 3l2.6 5.6 6 .7-4.5 4.1 1.2 6L12 16.4 6.7 19.4l1.2-6L3.4 9.3l6-.7z" fill="#fff"/></svg></div>
        <div class="service-name">Credit Repair</div>
        <p class="service-text">Assist you in removing defaults, judgments and incorrect information from your credit file.</p>
      </div>
      <div class="service">
        <div class="service-icon"><svg width="22" height="22" viewBox="0 0 24 24" aria-hidden="true"><rect x="3" y="8" width="18" height="12" rx="2" fill="none" stroke="#fff" stroke-width="2"/><path d="M9 8V5h6v3M3 13h18" fill="none" stroke="#fff" stroke-width="2"/></svg></div>
        <div class="service-name">Bankruptcy</div>
        <p class="service-text">We will work with you to accurately determine if bankruptcy is the right option for your situation.</p>
      </div>
      <div class="service">
        <div class="service-icon"><svg width="22" height="22" viewBox="0 0 24 24" aria-hidden="true"><rect x="3" y="6" width="18" height="13" rx="2" fill="none" stroke="#fff" stroke-width="2"/><path d="M3 10h18" stroke="#fff" stroke-width="2.5"/><path d="M6 15h5" stroke="#fff" stroke-width="1.6"/></svg></div>
        <div class="service-name">Bad Credit Loans</div>
        <p class="service-text">We work in your best interests to provide a consolidation loan that turns your bad credit history around.</p>
      </div>
    </div>
  </section>

  <section class="testimonials">
    <h2 class="section-title">Here's What Our Valued <span class="accent">Customers</span> Have To Say About Us</h2>
    <div class="arrow prev"><svg width="8" height="8" viewBox="0 0 10 10" aria-hidden="true"><path d="M6.5 1.5 3 5l3.5 3.5" fill="none" stroke="#7a8290" stroke-width="1.5"/></svg></div>
    <div class="arrow next"><svg width="8" height="8" viewBox="0 0 10 10" aria-hidden="true"><path d="M3.5 1.5 7 5 3.5 8.5" fill="none" stroke="#7a8290" stroke-width="1.5"/></svg></div>
    <div class="quote-row">
      <article class="quote-card">
        <div class="quote-head">
          <div class="avatar" role="img" aria-label="Customer portrait"></div>
          <div class="quote-name">Marlene, Box Hill, VIC</div>
        </div>
        <p class="quote-text">“We were on the verge of losing our car and did not know what to do, but now we are in an affordable arrangement to catch up on our car payments and are on our way to a debt free future. We are ever thankful.”</p>
      </article>
      <article class="quote-card">
        <div class="quote-head">
          <div class="avatar" role="img" aria-label="Customer portrait"></div>
          <div class="quote-name">Delia, Hawthorn, NSW</div>
        </div>
        <p class="quote-text">“I am very relieved and can now get my life on track. I am sincerely appreciative of all your assistance, you treated me like a person and never made me feel small for the situation I was in.”</p>
      </article>
    </div>
  </section>

  <section class="consultation" role="img" aria-label="Photo of paperwork and a calculator on a desk, in soft grey-blue tones">
    <h2 class="form-title">Free <span class="accent">Consultation</span></h2>
    <p class="form-intro">Please fill in the form below and we will get back to you within 24 hours.</p>
    <div class="lead-form">
      <div class="field">Name</div>
      <div class="field">Email</div>
      <div class="field">Phone Number</div>
      <div class="field">State</div>
      <div class="field">Your Overall Debt</div>
      <div class="field">Best Time to Contact</div>
    </div>
    <span class="btn">GET MY FREE CONSULTATION</span>
  </section>

  <footer class="site-footer">© 2015 Clear Path Ledger. All Rights Reserved</footer>

</div>
</body>
</html>
```